Redesign Current Website Into An Exciting Updated Design

We need to redesign the current website www.gleamvoucherhub.com We want an overall new look. We are rebranding so it will be a new logo and we would like to see new images as well so you cannot compare the old from the new.

You can use same exact content as on current url www.gleamvoucherhub.com

The website must be warm and inviting and fun yet professional and modern.

The website must also be designed with mobile in mind

The website must be warm and inviting yet professional and modern.

The website must also be designed with mobile in mind.

Target Market(s)

Consumers redeeming rewards

Industry/Entity Type

Promotional Reward Fullfillment

Coding

Coded - Design and coding required

Number of Pages Required

3 page

Requirements
Must have
• This website is a website where consumers come to redeem rewards they received from doing business with a company that offers these rewards. So the website should be very inviting.
Nice to have
• open
Should not have
• open

```html
<!DOCTYPE html>
<html lang="en">
<head>
<meta charset="utf-8">
<title>Gleam Voucher Hub — Redeem Your Rewards</title>
<link href="https://fonts.googleapis.com/css2?family=Poppins:wght@300;400;500;600;700&family=Roboto+Condensed:wght@600;700;800&display=swap" rel="stylesheet">
<style>
:root{
  --primary:#2b5f91;
  --primary-dark:#1f4d7a;
  --ink:#1e2f4a;
  --text:#5d6675;
  --muted:#8b93a1;
  --soft:#f5f7fa;
  --soft-blue:#e3f1fb;
  --line:#e4e8ee;
  --footer:#1e2a3a;
  --white:#fff;
}
*{box-sizing:border-box;margin:0;padding:0}
html,body{width:1200px;height:4202px;overflow:hidden}
body{font-family:'Poppins',sans-serif;color:var(--text);background:var(--white);position:relative}
section,header,footer{position:absolute;left:0;width:1200px}
.abs{position:absolute}
.eyebrow{font-family:'Roboto Condensed',sans-serif;font-weight:700;color:var(--primary);font-size:12px}
.eyebrow-icon{display:block;width:22px;height:14px;border:1.5px solid var(--primary);border-radius:7px 7px 2px 2px;margin-bottom:4px}
.center{text-align:center;left:0;width:1200px}
.center .eyebrow-icon{margin:0 auto 4px}
.section-title{font-weight:500;color:var(--ink)}
.photo{border-radius:2px}

/* header */
.site-header{top:0;height:80px;border-bottom:1px solid var(--line);background:var(--white)}
.brand{left:104px;top:22px;display:flex;align-items:center;gap:8px}
.brand-mark{width:22px;height:22px;border:2px solid var(--primary);flex:none}
.brand-name{font-weight:600;font-size:13px;line-height:1.15;color:var(--primary);width:92px}
.nav a{position:absolute;top:32px;font-size:11px;color:var(--muted);text-decoration:none}
.nav a.active{color:var(--primary);font-weight:500}
.btn-quote{left:947px;top:26px;width:153px;height:30px;background:var(--primary);color:#fff;font-size:12px;font-weight:600;display:flex;align-items:center;justify-content:center;border-radius:2px}

/* hero */
.hero{top:80px;height:585px;overflow:hidden}
.hero-photo{inset:0;background:
  radial-gradient(ellipse 120px 160px at 66% 78%,rgba(222,60,80,.85) 0,rgba(222,60,80,0) 100%),
  radial-gradient(ellipse 90px 120px at 52% 85%,rgba(238,180,195,.9) 0,rgba(238,180,195,0) 100%),
  radial-gradient(ellipse 110px 90px at 96% 88%,rgba(214,50,78,.85) 0,rgba(214,50,78,0) 100%),
  radial-gradient(ellipse 80px 260px at 65% 45%,rgba(46,40,44,.75) 0,rgba(46,40,44,0) 100%),
  radial-gradient(ellipse 80px 260px at 88% 45%,rgba(54,72,98,.65) 0,rgba(54,72,98,0) 100%),
  radial-gradient(ellipse 220px 200px at 80% 18%,rgba(176,98,80,.9) 0,rgba(176,98,80,0) 100%),
  linear-gradient(180deg,#9dbbd9 0%,#c39b88 45%,#a86b55 75%,#8a6a58 100%)}
.hero-fade{inset:0;background:linear-gradient(90deg,#fff 0%,rgba(255,255,255,.95) 30%,rgba(255,255,255,.4) 48%,rgba(255,255,255,0) 60%),linear-gradient(0deg,rgba(255,255,255,.5) 0%,rgba(255,255,255,0) 20%)}
.hero-welcome{left:101px;top:49px;font-size:10px;color:var(--ink);font-weight:500}
.hero-title{left:101px;top:64px;font-family:'Roboto Condensed',sans-serif;font-weight:800;color:var(--primary);font-size:42px;line-height:45px;width:460px}
.hero-text{left:101px;top:215px;width:380px;font-size:12px;line-height:15px;color:var(--ink)}
.redeem-card{left:101px;top:272px;width:292px;height:215px;background:#fff;border-radius:6px;box-shadow:0 6px 20px rgba(30,47,74,.12);padding:16px 12px}
.redeem-card h3{font-size:13px;font-weight:500;color:var(--primary);margin-bottom:14px}
.redeem-card label{display:block;font-size:9px;color:var(--ink);margin-bottom:6px}
.field{height:28px;background:#f1f3f6;border:1px solid var(--line);border-radius:3px;font-size:8px;color:var(--muted);display:flex;align-items:center;gap:8px;padding:0 10px;margin-bottom:14px}
.field i{width:12px;height:9px;border:1px solid var(--muted);border-radius:1px}
.btn-redeem{height:30px;background:var(--primary);color:#fff;font-size:12px;font-weight:600;display:flex;align-items:center;justify-content:center;border-radius:2px;margin-top:18px}

/* categories */
.categories{top:665px;height:590px;background:var(--soft)}
.cat-head{top:52px}
.cat-head h2{font-size:25px;line-height:28px;margin-top:2px}
.cat{top:191px;height:337px;border-radius:4px;overflow:hidden}
.cat-feature{left:137px;width:313px;background:var(--soft-blue)}
.cat-feature h3{position:absolute;left:15px;top:34px;font-size:24px;line-height:30px;font-weight:500;color:var(--primary)}
.cat-arrow{position:absolute;left:238px;top:48px;width:32px;height:32px;border:1.5px solid var(--primary);border-radius:50%}
.cat-photo{left:15px;top:128px;width:283px;height:188px;background:
  radial-gradient(ellipse 22px 40px at 52% 72%,rgba(246,200,40,.95) 0,rgba(246,200,40,0) 100%),
  radial-gradient(ellipse 150px 45px at 45% 50%,rgba(58,120,60,.95) 0,rgba(58,120,60,0) 100%),
  radial-gradient(ellipse 180px 50px at 30% 92%,rgba(84,120,70,.95) 0,rgba(84,120,70,0) 100%),
  linear-gradient(180deg,#5a9fd6 0%,#a9d3ef 32%,#3fa6c2 46%,#1f8aa8 62%,#6b7a6a 100%)}
.cat-slim{width:134px}
.cat-slim .vert{position:absolute;left:18px;bottom:90px;writing-mode:vertical-rl;transform:rotate(180deg);font-size:20px;font-weight:500;opacity:.18;white-space:nowrap}
.cat-slim svg{position:absolute;left:14px;top:258px}
.cat-slim span{position:absolute;left:14px;top:300px;font-size:10px;font-weight:600;line-height:12px}
.c-orange{left:470px;background:#fff6e6;color:#f39c12}
.c-green{left:623px;background:#e9f7ea;color:#3aa655}
.c-purple{left:776px;background:#f3efff;color:#8a5cf6}
.c-red{left:929px;background:#fdeeee;color:#e0504f}

/* steps */
.steps{top:1255px;height:518px;background:#fff}
.steps-head{top:32px}
.steps-head h2{font-size:25px;margin-top:6px}
.step{left:101px;width:623px;height:78px;background:#fff;border-radius:4px;box-shadow:0 3px 16px rgba(30,47,74,.08)}
.step-num{position:absolute;left:10px;top:13px;width:52px;height:52px;border-radius:50%;background:var(--primary-dark);color:#fff;font-weight:700;font-size:17px;display:flex;align-items:center;justify-content:center}
.step h3{position:absolute;left:77px;top:14px;font-size:13px;font-weight:500;color:var(--primary)}
.step p{position:absolute;left:77px;top:36px;width:535px;font-size:9.5px;line-height:15px;color:var(--muted)}
.step-line{left:135px;width:0;border-left:1.5px dotted var(--muted)}
.steps-art{left:733px;top:147px;width:392px;height:277px;background:
  radial-gradient(ellipse 45px 35px at 47% 28%,rgba(43,95,145,.55) 0,rgba(43,95,145,0) 100%),
  radial-gradient(ellipse 30px 110px at 28% 55%,rgba(40,52,70,.35) 0,rgba(40,52,70,0) 100%),
  radial-gradient(ellipse 30px 110px at 70% 55%,rgba(40,52,70,.35) 0,rgba(40,52,70,0) 100%),
  radial-gradient(ellipse 60px 70px at 12% 30%,rgba(210,214,220,.8) 0,rgba(210,214,220,0) 100%),
  radial-gradient(ellipse 50px 90px at 88% 55%,rgba(220,223,228,.9) 0,rgba(220,223,228,0) 100%),
  linear-gradient(180deg,#fff 0%,#f3f5f8 85%,#e6e9ee 86%,#fff 100%)}

/* about */
.about{top:1773px;height:558px;background:var(--soft)}
.deco{background:#dbe9f6}
.collage-img{border:6px solid #fff;box-shadow:0 4px 14px rgba(0,0,0,.08)}
.about-text{left:606px;top:70px;width:500px}
.about-text h2{font-size:24px;margin:4px 0 14px}
.about-text p{font-size:10.3px;line-height:15.4px;color:var(--muted);margin-bottom:11px}
.features{display:flex;gap:26px;margin-top:18px;font-size:10.5px;color:var(--ink)}
.features div{display:flex;align-items:center;gap:8px}
.features i{width:32px;height:32px;border-radius:4px;background:#e3ecf5;position:relative}
.features i:after{content:"";position:absolute;inset:9px;border:1.5px solid var(--primary);border-radius:2px}
.read-more{margin-top:20px;font-size:12px;color:var(--primary);display:flex;align-items:center;gap:8px}

/* testimonials */
.testimonials{top:2331px;height:502px;background:#f4f6f9}
.testi-head{left:101px;top:46px}
.testi-head h2{font-size:35px;line-height:39px;margin-top:4px}
.quote-mark{left:101px;top:200px;font-size:40px;color:var(--primary);font-family:Georgia,serif;line-height:1}
.testi-quote{left:101px;top:247px;width:400px;font-size:14px;line-height:21px;color:var(--muted)}
.testi-name{left:101px;top:343px;font-size:10px;font-weight:600;color:var(--ink)}
.testi-loc{left:101px;top:359px;font-size:7px;color:var(--muted)}
.arrow-btn{top:395px;width:40px;height:40px;border-radius:3px;display:flex;align-items:center;justify-content:center}
.testi-photo{left:574px;top:76px;width:526px;height:351px;background:
  radial-gradient(ellipse 40px 110px at 38% 62%,rgba(60,40,50,.7) 0,rgba(60,40,50,0) 100%),
  radial-gradient(ellipse 260px 40px at 55% 42%,rgba(240,242,246,.9) 0,rgba(240,242,246,0) 100%),
  radial-gradient(ellipse 120px 30px at 20% 28%,rgba(40,70,130,.7) 0,rgba(40,70,130,0) 100%),
  radial-gradient(ellipse 300px 80px at 60% 58%,rgba(240,200,140,.7) 0,rgba(240,200,140,0) 100%),
  linear-gradient(180deg,#2f5d96 0%,#7fa5cc 30%,#e3c89a 52%,#b8895c 68%,#6e5038 100%)}

/* brands */
.brands{top:2833px;height:264px;background:#fff}
.brands-head{top:32px}
.brands-head h2{font-size:26px;line-height:28px;margin-top:4px}
.brand-tile{top:160px;width:157px;height:65px;border:1px solid var(--line);border-radius:3px;display:flex;align-items:center;justify-content:center;font-size:15px;font-weight:600;color:#444c58;background:#fff}

/* faq */
.faq{top:3097px;height:750px;background:var(--soft)}
.faq-head{left:101px;top:126px}
.faq-head h2{font-size:35px;line-height:40px;margin-top:6px}
.faq-desc{left:101px;top:264px;width:420px;font-size:10px;line-height:15px;color:var(--muted)}
.faq-item{left:101px;width:406px;background:#eceff3;border-radius:4px;font-size:10.5px;color:var(--ink);padding:0 16px;display:flex;align-items:center;justify-content:space-between}
.faq-item b{font-weight:300;color:var(--muted);font-size:18px}
.faq-open{background:var(--primary);color:#fff;display:block;padding:14px 16px}
.faq-open .q{display:flex;justify-content:space-between;font-size:10.5px}
.faq-open p{margin-top:20px;font-size:9.5px;line-height:14.5px;color:#d7e3f0}
.faq-photo{left:603px;top:62px;width:494px;height:626px;background:
  radial-gradient(ellipse 90px 150px at 75% 55%,rgba(150,50,60,.75) 0,rgba(150,50,60,0) 100%),
  radial-gradient(ellipse 110px 170px at 42% 58%,rgba(30,30,36,.85) 0,rgba(30,30,36,0) 100%),
  radial-gradient(ellipse 90px 130px at 14% 42%,rgba(70,90,110,.7) 0,rgba(70,90,110,0) 100%),
  radial-gradient(ellipse 260px 90px at 50% 12%,rgba(150,156,162,.8) 0,rgba(150,156,162,0) 100%),
  linear-gradient(180deg,#5a5e62 0%,#8e9296 28%,#5c524c 60%,#d8d2cb 78%,#c9c3bc 100%)}

/* footer */
.site-footer{top:3847px;height:355px;background:var(--footer);color:#c7ced8}
.footer-brand{left:101px;top:78px;display:flex;align-items:center;gap:10px}
.footer-brand .brand-mark{border-color:#fff;width:26px;height:26px}
.footer-brand .brand-name{color:#fff;font-size:16px;width:120px}
.f-col h4{font-size:16px;font-weight:600;color:#fff;margin-bottom:20px}
.f-col a{display:block;font-size:12px;color:#c7ced8;text-decoration:none;margin-bottom:15px}
.f-input{left:771px;top:121px;width:248px;height:31px;border:1px solid #4a5668;border-radius:3px;background:#2a3647;font-size:11px;color:#8b93a1;padding:0 12px;display:flex;align-items:center}
.f-send{left:1030px;top:121px;width:33px;height:31px;background:var(--primary);border-radius:3px;display:flex;align-items:center;justify-content:center}
.social{top:173px;width:26px;height:26px;border-radius:50%;border:1px solid #6b7789}
.copyright{top:309px;left:0;width:1200px;text-align:center;font-size:11px;color:#c7ced8}
.copyright b{color:#fff;font-weight:600}
</style>
</head>
<body>

<header class="site-header">
  <div class="brand abs"><span class="brand-mark"></span><span class="brand-name">Gleam Voucher Hub</span></div>
  <nav class="nav">
    <a class="active" style="left:541px">Home</a>
    <a style="left:603px">Rewards</a>
    <a style="left:678px">How It Work</a>
    <a style="left:773px">About Us</a>
    <a style="left:851px">FAQ's</a>
  </nav>
  <div class="btn-quote abs">Get A Free Quote</div>
</header>

<section class="hero">
  <div class="hero-photo abs" role="img" aria-label="Two smiling women carrying red and pink shopping bags on a sunny city street"></div>
  <div class="hero-fade abs"></div>
  <p class="hero-welcome abs">Welcome to Gleam Voucher Hub</p>
  <h1 class="hero-title abs">Transform Your Rewards into Memorable Experiences</h1>
  <p class="hero-text abs">Redeem your promotional certificates for exclusive travel, dining, and lifestyle rewards. Start your journey today.</p>
  <form class="redeem-card abs">
    <h3>Start Your Redemption</h3>
    <label>Certificate Number</label>
    <div class="field"><i></i>Enter your certificate number</div>
    <label>Email Address</label>
    <div class="field"><i></i>Enter your email</div>
    <div class="btn-redeem">Redeem Now</div>
  </form>
</section>

<section class="categories">
  <div class="cat-head abs center">
    <span class="eyebrow-icon"></span>
    <span class="eyebrow">Exclusive Reward Categories</span>
    <h2 class="section-title">Choose From Our Curated Selection<br>Of Premium Rewards</h2>
  </div>
  <div class="cat cat-feature abs">
    <h3>Vacation<br>Certificates</h3>
    <svg class="cat-arrow" viewBox="0 0 32 32"><path d="M11 21L21 11M13 11h8v8" fill="none" stroke="#2b5f91" stroke-width="1.5"/></svg>
    <div class="cat-photo abs photo" role="img" aria-label="Traveller in a yellow dress overlooking a green tropical island and turquoise sea"></div>
  </div>
  <div class="cat cat-slim c-orange abs"><span class="vert">Travel Vouchers</span>
    <svg width="34" height="34" viewBox="0 0 34 34" fill="none" stroke="#f39c12" stroke-width="2"><rect x="4" y="9" width="26" height="18" rx="2"/><path d="M4 15h26M12 9V5h10v4"/></svg>
    <span>Travel<br>Vouchers</span></div>
  <div class="cat cat-slim c-green abs"><span class="vert">Digital Electronic Products</span>
    <svg width="34" height="34" viewBox="0 0 34 34" fill="none" stroke="#3aa655" stroke-width="2"><rect x="6" y="4" width="16" height="22" rx="2"/><rect x="18" y="14" width="12" height="16" rx="2"/><path d="M4 30h26"/></svg>
    <span>Digital<br>Electronic Products</span></div>
  <div class="cat cat-slim c-purple abs"><span class="vert">Dining Incentives</span>
    <svg width="34" height="34" viewBox="0 0 34 34" fill="none" stroke="#8a5cf6" stroke-width="2"><path d="M4 18h26M8 18v12M26 18v12M10 4v8M14 4v8M12 12v6M22 4c-3 2-3 8 0 10v4"/></svg>
    <span>Dining<br>Incentives</span></div>
  <div class="cat cat-slim c-red abs"><span class="vert">Gas &amp; Grocery Rewards</span>
    <svg width="34" height="34" viewBox="0 0 34 34" fill="none" stroke="#e0504f" stroke-width="2"><path d="M3 6h5l4 16h16l3-12H10"/><circle cx="14" cy="28" r="2"/><circle cx="25" cy="28" r="2"/></svg>
    <span>Gas &amp; Grocery<br>Rewards</span></div>
</section>

<section class="steps">
  <div class="steps-head abs center">
    <span class="eyebrow">How It Work</span>
    <h2 class="section-title">Simple Steps Redeem Your Rewards</h2>
  </div>
  <div class="step-line abs" style="top:184px;height:250px"></div>
  <div class="step abs" style="top:119px"><div class="step-num">1.</div><h3>Enter Certificate</h3><p>Input Your Unique Certificate Number And Registered Email Address Into The Redemption Portal. This Step Verifies Your Eligibility And Unlocks Your Available Rewards.</p></div>
  <div class="step abs" style="top:245px"><div class="step-num">2.</div><h3>Choose Your Reward</h3><p>Browse Through A Variety Of Reward Options, Including Vacation Certificates, Travel Vouchers, Dining Incentives, &amp; More. Select The Reward That Best Suits Your Preferences.</p></div>
  <div class="step abs" style="top:370px"><div class="step-num">3.</div><h3>Enjoy Your Reward</h3><p>Receive A Confirmation Email With Redemption Details And Next Steps. Follow Any Additional Instructions To Complete The Process And Enjoy Your Reward Hassle-Free!</p></div>
  <div class="steps-art abs" role="img" aria-label="Illustration of one person handing a blue wrapped gift box to another in a bright room"></div>
</section>

<section class="about">
  <div class="deco abs" style="left:225px;top:37px;width:36px;height:36px"></div>
  <div class="deco abs" style="left:101px;top:190px;width:24px;height:24px"></div>
  <div class="deco abs" style="left:101px;top:370px;width:14px;height:14px"></div>
  <div class="deco abs" style="left:509px;top:437px;width:36px;height:36px"></div>
  <div class="collage-img abs" style="left:105px;top:61px;width:139px;height:130px;background:radial-gradient(ellipse 50px 40px at 60% 50%,rgba(240,236,225,.9) 0,rgba(240,236,225,0) 100%),linear-gradient(135deg,#2f4a5c 0%,#7a6a4e 55%,#c7964f 100%)" role="img" aria-label="Team hands working over documents on a table"></div>
  <div class="collage-img abs" style="left:137px;top:144px;width:351px;height:231px;background:radial-gradient(ellipse 70px 110px at 22% 65%,rgba(120,170,190,.85) 0,rgba(120,170,190,0) 100%),radial-gradient(ellipse 60px 40px at 82% 20%,rgba(220,80,60,.8) 0,rgba(220,80,60,0) 100%),radial-gradient(ellipse 90px 100px at 60% 60%,rgba(90,80,75,.6) 0,rgba(90,80,75,0) 100%),linear-gradient(135deg,#e6ddd0 0%,#b9a891 50%,#8c6e55 100%)" role="img" aria-label="Colleagues celebrating a birthday together in an office"></div>
  <div class="collage-img abs" style="left:299px;top:294px;width:232px;height:153px;background:radial-gradient(ellipse 50px 40px at 78% 80%,rgba(235,200,90,.9) 0,rgba(235,200,90,0) 100%),radial-gradient(ellipse 50px 60px at 28% 55%,rgba(200,60,60,.8) 0,rgba(200,60,60,0) 100%),linear-gradient(135deg,#f2ece4 0%,#e2c7a6 55%,#cf9a66 100%)" role="img" aria-label="Two women laughing at a laptop"></div>
  <div class="collage-img abs" style="left:98px;top:376px;width:237px;height:141px;background:radial-gradient(ellipse 140px 40px at 50% 70%,rgba(60,60,70,.8) 0,rgba(60,60,70,0) 100%),radial-gradient(ellipse 160px 30px at 50% 92%,rgba(220,170,60,.7) 0,rgba(220,170,60,0) 100%),linear-gradient(180deg,#27478a 0%,#4b6aa8 35%,#8a8f9a 65%,#3a3a40 100%)" role="img" aria-label="Business group seated together at a conference"></div>
  <div class="about-text abs">
    <span class="eyebrow-icon"></span>
    <span class="eyebrow">About Us</span>
    <h2 class="section-title">Who We Are &amp; What We Do</h2>
    <p>We Provide Businesses With Marketing Incentives In The Form Of Gift Certificates And Vouchers Redeemable For Discounts On Travel, Smart Devices, Dining, Golf, And More. Thousands Of Companies Worldwide Use Our Incentives For Promotions, Customer Loyalty Programs, Contests, And Appreciation Gifts.</p>
    <p>As A Third-Party Administrator, We Handle The Redemption And Fulfillment Of These Incentives Through Our User-Friendly Online Platform. Customers Simply Enter Their Code And Email To Redeem Their Offer And Complete The Fulfillment Process.</p>
    <p>We Do Not Market Directly To End Users; Instead, Our Incentives Are Exclusively Distributed By Businesses As Part Of Their Marketing Strategies. Our Role Is To Facilitate Redemption While Ensuring Compliance With The Offer's Terms And Conditions Set By Our Vendor Partners.</p>
    <div class="features">
      <div><i></i>Easy Redemption</div>
      <div><i></i>Trusted By Businesses</div>
      <div><i></i>Diverse Rewards</div>
    </div>
    <div class="read-more">Read More <svg width="26" height="8" viewBox="0 0 26 8"><path d="M0 4h24M20 1l4 3-4 3" fill="none" stroke="#2b5f91" stroke-width="1.2"/></svg></div>
  </div>
</section>

<section class="testimonials">
  <div class="testi-head abs">
    <span class="eyebrow-icon"></span>
    <span class="eyebrow">Our Clients</span>
    <h2 class="section-title">Real Experience From<br>Satisfy Customers</h2>
  </div>
  <div class="quote-mark abs">&#8220;</div>
  <p class="testi-quote abs">"This guy is true professional and very experienced in migration and server configuration. He was able to complete my order in time and as per agreed scope. Highly recommend!"</p>
  <p class="testi-name abs">Marlo T.</p>
  <p class="testi-loc abs">Lakeview</p>
  <div class="arrow-btn abs" style="left:101px;background:#e3ecf5"><svg width="16" height="10" viewBox="0 0 16 10"><path d="M16 5H2M6 1L2 5l4 4" fill="none" stroke="#2b5f91" stroke-width="1.5"/></svg></div>
  <div class="arrow-btn abs" style="left:150px;background:var(--primary)"><svg width="16" height="10" viewBox="0 0 16 10"><path d="M0 5h14M10 1l4 4-4 4" fill="none" stroke="#fff" stroke-width="1.5"/></svg></div>
  <div class="testi-photo abs photo" role="img" aria-label="Traveller with a backpack walking beside a small white private plane at golden sunset"></div>
</section>

<section class="brands">
  <div class="brands-head abs center">
    <span class="eyebrow-icon"></span>
    <span class="eyebrow">Trusted By Leading Brands</span>
    <h2 class="section-title">Trusted By Businesses Worldwide For Reward<br>Redemption And Fulfillment</h2>
  </div>
  <div class="brand-tile abs" style="left:-26px">Northbeam</div>
  <div class="brand-tile abs" style="left:156px">Veltora</div>
  <div class="brand-tile abs" style="left:338px">HomeCart</div>
  <div class="brand-tile abs" style="left:520px">Ashford Realty</div>
  <div class="brand-tile abs" style="left:702px">Kestrel Homes</div>
  <div class="brand-tile abs" style="left:885px">Carewell</div>
  <div class="brand-tile abs" style="left:1067px">Fieldstone</div>
</section>

<section class="faq">
  <div class="faq-head abs">
    <span class="eyebrow-icon"></span>
    <span class="eyebrow">FAQ's</span>
    <h2 class="section-title">Relax We're Always<br>Here For You!</h2>
  </div>
  <p class="faq-desc abs">Lorem Ipsum Dolor Sit Amet, Consectetur Adipiscing Elit, Sed Do Eiusmod Tempor Incididunt Ut Labore Et Dolore Magna Aliqua.</p>
  <div class="faq-item abs" style="top:318px;height:44px">How do I redeem my gift certificate or voucher?<b>+</b></div>
  <div class="faq-item faq-open abs" style="top:378px;height:116px">
    <div class="q"><span>What types of rewards can I redeem?</span><span>&#10005;</span></div>
    <p>Our marketing incentives include discounts on travel, smart devices, dining, golf, and more. The specific reward depends on the voucher received and its associated terms.</p>
  </div>
  <div class="faq-item abs" style="top:509px;height:44px">Can I transfer my voucher to someone else?<b>+</b></div>
  <div class="faq-item abs" style="top:569px;height:44px">Who do I contact if I need support?<b>+</b></div>
  <div class="faq-photo abs photo" role="img" aria-label="Friendly support adviser helping two customers at a laptop in a modern office"></div>
</section>

<footer class="site-footer">
  <div class="footer-brand abs"><span class="brand-mark"></span><span class="brand-name">Gleam Voucher Hub</span></div>
  <div class="f-col abs" style="left:347px;top:88px"><h4>Quick Links</h4><a>Home</a><a>Rewards</a><a>How It Works</a><a>About Us</a><a>FAQ'S</a></div>
  <div class="f-col abs" style="left:559px;top:88px"><h4>Information</h4><a>Terms &amp; Conditions</a><a>Privacy Policy</a><a>Careers</a></div>
  <div class="f-col abs" style="left:771px;top:88px"><h4>Subscribe</h4></div>
  <div class="f-input abs">Email</div>
  <div class="f-send abs"><svg width="14" height="14" viewBox="0 0 14 14"><path d="M1 7l12-6-4 12-2-5z" fill="none" stroke="#fff" stroke-width="1.2"/></svg></div>
  <div class="social abs" style="left:771px"></div>
  <div class="social abs" style="left:807px"></div>
  <div class="social abs" style="left:844px"></div>
  <div class="social abs" style="left:880px"></div>
  <p class="copyright abs">© Copyright 2005-2025. <b>Gleam Voucher Hub</b> All Rights Reserved.</p>
</footer>

</body>
</html>
```